Quenlo needs a CD cover artwork for the song "Quiet Harbors"

Hi, I need a CD cover artwork for my new song "Quiet Harbors". I want to have an image of "Earth" for it. The earth image can be either picturesque or unique artistic. And also, it needs to contain the logo "Quenlo" and "Quiet Harbors".
jpg. file is necessary.
And I don't like something purchased from the stock image which I need to pay additionally. Original image is preferable.

Target Market(s)

Music

Colors

Designer to choose colors to be used in the design.

Requirements
Must have
• -Earth image
• -The logo "Quenlo" and "Quiet Harbors"
Nice to have
• -A whole globe image of the earth might be good, rather than a part of the globe or scene of the earth.
• -Something awe-inspiring image might be good.
• -The logo "Quenlo" and "Quiet Harbors" better fuse to the image nicely rather than oddly standing out from the image.
Should not have
• -the stock image which I need to pay additionally

```html
<!DOCTYPE html>
<html lang="en">
<head>
<meta charset="utf-8">
<title>Quenlo – Quiet Harbors</title>
<link rel="stylesheet" href="https://fonts.googleapis.com/css2?family=Arimo:wght@700&family=Oswald:wght@400;500&display=swap">
<style>
  :root {
    --space-deep: #070826;
    --space-navy: #121a5c;
    --space-blue: #2433a6;
    --space-violet: #4b2a8c;
    --haze-teal: #5fa6b8;
    --haze-pink: #c36fd0;
    --globe-ocean: #1f5fc4;
    --globe-ocean-deep: #0c2a78;
    --globe-land: #7fbf3a;
    --globe-sand: #d8d39a;
    --globe-glow: #f4d2ff;
    --type-white: #ffffff;
  }
  * { margin: 0; padding: 0; box-sizing: border-box; }
  html, body {
    width: 1200px;
    height: 1200px;
    overflow: hidden;
    background: var(--space-deep);
  }
  .cover {
    position: relative;
    width: 1200px;
    height: 1200px;
    overflow: hidden;
  }
  .cover__space {
    position: absolute;
    inset: 0;
    width: 1200px;
    height: 1200px;
  }
  .cover__artist {
    position: absolute;
    top: 44px;
    left: 0;
    width: 1200px;
    text-align: center;
    font-family: "Arimo", Arial, sans-serif;
    font-weight: 700;
    font-size: 122px;
    line-height: 1;
    letter-spacing: 0.11em;
    padding-left: 0.11em;
    color: var(--type-white);
  }
  .cover__title {
    position: absolute;
    top: 160px;
    left: 0;
    width: 1200px;
    text-align: center;
    font-family: "Oswald", "Arial Narrow", sans-serif;
    font-weight: 500;
    font-size: 86px;
    line-height: 1;
    letter-spacing: -0.01em;
    color: var(--type-white);
    transform: scaleX(0.8);
  }
  .cover__globe {
    position: absolute;
    left: 374px;
    top: 374px;
    width: 444px;
    height: 444px;
    border-radius: 50%;
    box-shadow:
      0 0 10px 3px var(--globe-glow),
      0 0 40px 14px rgba(214, 140, 230, 0.55),
      0 0 110px 40px rgba(195, 111, 208, 0.28);
  }
</style>
</head>
<body>
  <main class="cover">
    <svg class="cover__space" viewBox="0 0 1200 1200" role="img" aria-label="Deep space full of stars with a teal and violet nebula ring around the planet">
      <defs>
        <radialGradient id="spaceBase" cx="50%" cy="50%" r="72%">
          <stop offset="0%" stop-color="#2c3cb4"/>
          <stop offset="45%" stop-color="#2433a6"/>
          <stop offset="78%" stop-color="#141c66"/>
          <stop offset="100%" stop-color="#070826"/>
        </radialGradient>
        <radialGradient id="hazeTeal" cx="50%" cy="50%" r="50%">
          <stop offset="0%" stop-color="#7cc3c8" stop-opacity="0.75"/>
          <stop offset="55%" stop-color="#5fa6b8" stop-opacity="0.35"/>
          <stop offset="100%" stop-color="#5fa6b8" stop-opacity="0"/>
        </radialGradient>
        <radialGradient id="hazePink" cx="50%" cy="50%" r="50%">
          <stop offset="0%" stop-color="#c36fd0" stop-opacity="0.7"/>
          <stop offset="60%" stop-color="#8a3fb0" stop-opacity="0.3"/>
          <stop offset="100%" stop-color="#4b2a8c" stop-opacity="0"/>
        </radialGradient>
        <radialGradient id="hazeViolet" cx="50%" cy="50%" r="50%">
          <stop offset="0%" stop-color="#6a3aa8" stop-opacity="0.55"/>
          <stop offset="100%" stop-color="#4b2a8c" stop-opacity="0"/>
        </radialGradient>
        <radialGradient id="hazeCore" cx="50%" cy="50%" r="50%">
          <stop offset="40%" stop-color="#e7b8f0" stop-opacity="0.55"/>
          <stop offset="70%" stop-color="#9a7ad0" stop-opacity="0.2"/>
          <stop offset="100%" stop-color="#2433a6" stop-opacity="0"/>
        </radialGradient>
      </defs>
      <rect width="1200" height="1200" fill="url(#spaceBase)"/>
      <ellipse cx="640" cy="380" rx="420" ry="200" fill="url(#hazeTeal)"/>
      <ellipse cx="980" cy="560" rx="260" ry="160" fill="url(#hazeTeal)" opacity="0.6"/>
      <ellipse cx="300" cy="720" rx="300" ry="220" fill="url(#hazePink)"/>
      <ellipse cx="780" cy="1080" rx="320" ry="140" fill="url(#hazeViolet)"/>
      <ellipse cx="160" cy="480" rx="200" ry="140" fill="url(#hazeTeal)" opacity="0.45"/>
      <circle cx="596" cy="596" r="330" fill="url(#hazeCore)"/>
    </svg>

    <h1 class="cover__artist">QUENLO</h1>
    <h2 class="cover__title">Quiet Harbors</h2>

    <svg class="cover__globe" viewBox="0 0 444 444" role="img" aria-label="The whole Earth seen from space, blue oceans and green continents under white clouds">
      <defs>
        <radialGradient id="globeOcean" cx="44%" cy="58%" r="62%">
          <stop offset="0%" stop-color="#4f8fe6"/>
          <stop offset="40%" stop-color="#1f5fc4"/>
          <stop offset="85%" stop-color="#0c2a78"/>
          <stop offset="100%" stop-color="#06174a"/>
        </radialGradient>
        <radialGradient id="globeLand" cx="52%" cy="30%" r="48%">
          <stop offset="0%" stop-color="#d8d39a" stop-opacity="0.95"/>
          <stop offset="40%" stop-color="#7fbf3a" stop-opacity="0.85"/>
          <stop offset="75%" stop-color="#4f9a2e" stop-opacity="0.35"/>
          <stop offset="100%" stop-color="#4f9a2e" stop-opacity="0"/>
        </radialGradient>
        <radialGradient id="globeCloud" cx="42%" cy="66%" r="30%">
          <stop offset="0%" stop-color="#ffffff" stop-opacity="0.5"/>
          <stop offset="100%" stop-color="#ffffff" stop-opacity="0"/>
        </radialGradient>
        <radialGradient id="globeShade" cx="36%" cy="40%" r="68%">
          <stop offset="70%" stop-color="#020a2a" stop-opacity="0"/>
          <stop offset="100%" stop-color="#020a2a" stop-opacity="0.7"/>
        </radialGradient>
      </defs>
      <circle cx="222" cy="222" r="222" fill="url(#globeOcean)"/>
      <circle cx="222" cy="222" r="222" fill="url(#globeLand)"/>
      <circle cx="222" cy="222" r="222" fill="url(#globeCloud)"/>
      <circle cx="222" cy="222" r="222" fill="url(#globeShade)"/>
    </svg>
  </main>
</body>
</html>
```